The name of my company is Tolmen Refacing LLC and I would like the sub text to say "Cabinet Refacing and Countertops". Have my name Dorian Tolmen, Owner / Sales, contact info: Cell: 360-555-0147 / Email: dorian.tolmen@quenmail.com

Simple, Clean, and Organized. With colors that will appeal to the eye.

Target Market(s)

Houses and Apartments

Industry/Entity Type

Cabinet Refacing

Contact Information for Business Card

Company name and sub text Dorian Tolmen - Owner / Sales, my cell phone number and email

Requirements
Must have
• Business name, my name / position, and my contact info
Nice to have
• Simple. Organized. Appealing to the eye

```html
<!DOCTYPE html>
<html lang="en">
<head>
<meta charset="utf-8">
<title>Tolmen Refacing LLC – Business Card</title>
<link rel="stylesheet" href="https://fonts.googleapis.com/css2?family=Montserrat:wght@300;500;600;700&family=Barlow+Semi+Condensed:wght@500;600&display=swap">
<style>
  :root {
    --backdrop: #d1d2d4;
    --leaf: #72bf4c;
    --leaf-deep: #63994f;
    --ink: #16122f;
    --night: #15112e;
    --night-soft: #1f2536;
  }
  * { box-sizing: border-box; margin: 0; padding: 0; }
  html, body {
    width: 1200px; height: 1199px; overflow: hidden;
    background: var(--backdrop);
  }
  .card {
    position: absolute; left: 240px;
    width: 727px; height: 415px;
    overflow: hidden;
  }

  /* Front */
  .card--front { top: 162px; background: var(--leaf); color: var(--ink); }
  .front-decor {
    position: absolute; left: 0; top: 0; width: 410px; height: 100%;
    background: linear-gradient(100deg, var(--leaf-deep) 0%, var(--leaf-deep) 22%, rgba(99,153,79,0.55) 45%, rgba(114,191,76,0) 80%);
  }
  .front-mark {
    position: absolute; left: 336px; top: 40px;
    width: 56px; height: 56px; border-radius: 50%;
    background: var(--ink);
  }
  .front-lockup {
    position: absolute; left: 0; right: 0; top: 110px; text-align: center;
  }
  .front-lockup .name {
    font-family: "Montserrat", sans-serif; font-weight: 300;
    font-size: 21px; letter-spacing: 0.2px; line-height: 1;
  }
  .front-lockup .sub {
    font-family: "Barlow Semi Condensed", sans-serif; font-weight: 600;
    font-size: 11px; margin-top: 5px; letter-spacing: 0.2px;
  }
  .title-block {
    position: absolute; left: 109px; top: 206px; width: 508px; height: 66px;
    border-left: 2px solid var(--ink); border-right: 2px solid var(--ink);
    padding-left: 16px; white-space: nowrap;
  }
  .title-block .title {
    font-family: "Montserrat", sans-serif; font-weight: 700;
    font-size: 35px; line-height: 38px; letter-spacing: 0.2px;
  }
  .title-block .tagline {
    font-family: "Montserrat", sans-serif; font-weight: 600;
    font-size: 14px; letter-spacing: 5.4px; margin-top: 7px;
  }
  .owner {
    position: absolute; left: 0; right: 0; top: 304px; text-align: center;
    font-family: "Montserrat", sans-serif; font-weight: 600;
    font-size: 14px; letter-spacing: 1.5px;
  }
  .owner .role { font-weight: 500; }
  .contact {
    position: absolute; top: 357px;
    display: flex; align-items: center; gap: 9px;
    font-family: "Montserrat", sans-serif; font-weight: 600; font-size: 16px;
    white-space: nowrap;
  }
  .contact--phone { left: 109px; }
  .contact--email { left: 372px; }
  .contact svg { display: block; }

  /* Back */
  .card--back { top: 654px; background: var(--night); color: var(--leaf); }
  .back-decor {
    position: absolute; inset: 0;
    background: var(--night-soft);
    clip-path: polygon(100% 2%, 100% 100%, 40% 100%, 62% 60%, 78% 22%);
  }
  .back-mark {
    position: absolute; left: 318px; top: 112px;
    width: 92px; height: 92px; border-radius: 50%;
    background: var(--leaf);
  }
  .back-lockup {
    position: absolute; left: 0; right: 0; top: 236px; text-align: center;
    white-space: nowrap;
  }
  .back-lockup .name {
    font-family: "Montserrat", sans-serif; font-weight: 300;
    font-size: 36px; line-height: 1; letter-spacing: 0.4px;
  }
  .back-lockup .sub {
    font-family: "Barlow Semi Condensed", sans-serif; font-weight: 500;
    font-size: 19px; margin-top: 8px; letter-spacing: 0.3px;
  }
</style>
</head>
<body>

<section class="card card--front">
  <div class="front-decor" role="img" aria-label="Faint decorative brand shape in darker green"></div>
  <div class="front-mark"></div>
  <div class="front-lockup">
    <div class="name">TOLMEN REFACING LLC</div>
    <div class="sub">CABINET REFACING AND COUNTERTOPS</div>
  </div>
  <div class="title-block">
    <div class="title">TOLMEN REFACING LLC</div>
    <div class="tagline">CABINET REFACING AND COUNTERTOPS</div>
  </div>
  <div class="owner">DORIAN TOLMEN <span class="role">– OWNER / SALES</span></div>
  <div class="contact contact--phone">
    <svg width="22" height="22" viewBox="0 0 24 24" fill="none" stroke="currentColor" stroke-width="1.6" stroke-linejoin="round">
      <path d="M5 3h4l2 5-2.5 1.5a11 11 0 0 0 6 6L16 13l5 2v4a2 2 0 0 1-2 2A16 16 0 0 1 3 5a2 2 0 0 1 2-2z"/>
      <path d="M14 3a7 7 0 0 1 7 7M14 6.5a3.5 3.5 0 0 1 3.5 3.5"/>
    </svg>
    <span>360-555-0147</span>
  </div>
  <div class="contact contact--email">
    <svg width="24" height="18" viewBox="0 0 24 18" fill="none" stroke="currentColor" stroke-width="1.6">
      <rect x="1" y="1" width="22" height="16"/>
      <path d="M1 1l11 9 11-9M1 17l8-7M23 17l-8-7"/>
    </svg>
    <span>dorian.tolmen@quenmail.com</span>
  </div>
</section>

<section class="card card--back">
  <div class="back-decor" role="img" aria-label="Large faint decorative brand shape in slate"></div>
  <div class="back-mark"></div>
  <div class="back-lockup">
    <div class="name">TOLMEN REFACING LLC</div>
    <div class="sub">CABINET REFACING AND COUNTERTOPS</div>
  </div>
</section>

</body>
</html>
```